Meridel Bidding Group Website

We are an food equipment auction company and are in need of an updated website. Old website found here: http://meridelbiddinggroup.example/ . We need to be able to share upcoming auctions, past auctions, companies we've worked with, needs to be mobile friendly. We will also need an easy to access back office where we can add new info, auction info, etc.

Target Market(s)

Equipment auctions, large food manufacturers, equipment resalers

Industry/Entity Type

Auction

Coding

Number of Pages Required

5+ page

Font styles to use
Sans Serif

Colors
acd136
ffffff

Requirements
Must have
• Back office where we can add new auctions
-mobile friendly
-contact us page,
-services page
-social media widgets
-must match our current logo
-current auctions on front page
- join mailing list
- past auctions / current auctions pages
Nice to have
• Would like it to be clean design, easy to view and find options, modern

```html
<!DOCTYPE html>
<html lang="en">
<head>
<meta charset="utf-8">
<title>Meridel Bidding Group</title>
<link rel="stylesheet" href="https://fonts.googleapis.com/css2?family=Roboto:wght@400;500;700&display=swap">
<style>
:root{
  --green:#8dc63f;
  --green-band:#93c83e;
  --grey-title:#55585b;
  --ink:#222;
  --card-border:#e3e3e3;
  --btn-grey:#5f6368;
  --light-bg:#f3f6f9;
  --footer:#1e1e1e;
  --white:#fff;
}
*{box-sizing:border-box;margin:0;padding:0}
html,body{width:1200px;height:4471px;overflow:hidden;background:var(--white);font-family:"Roboto",Arial,sans-serif;color:var(--ink)}
.page{position:relative;width:1200px;height:4471px}
section,header,footer{position:absolute;left:0;width:1200px}
.abs{position:absolute}

/* header */
.site-header{top:0;height:90px;background:#fff;border-bottom:3px solid var(--green)}
.brand{left:100px;top:16px;display:flex;align-items:center;gap:12px}
.brand-mark{width:44px;height:44px;background:var(--green)}
.brand-name{font-weight:700;font-size:22px;line-height:24px;color:var(--grey-title);text-transform:uppercase}
.phone{left:660px;top:11px;display:flex;align-items:center;gap:8px;font-size:17px;font-weight:500}
.phone-icon{width:34px;height:34px;border:2px solid var(--green);border-radius:50%;display:flex;align-items:center;justify-content:center}
.finder-btn{left:842px;top:9px;width:170px;height:38px;background:var(--green);color:#fff;font-size:13px;font-weight:500;display:flex;align-items:center;justify-content:center;text-transform:uppercase}
.lang{left:1030px;top:10px;width:70px;height:36px;border:1px solid #ddd;display:flex;align-items:center;justify-content:center;font-size:12px;gap:6px}
.nav-item{position:absolute;top:61px;width:110px;margin-left:-55px;text-align:center;font-size:14px;font-weight:500;line-height:16px;color:#222;text-transform:uppercase}
.nav-item.home{color:var(--green)}
.home-icon{position:absolute;left:465px;top:39px}

/* hero */
.hero{top:90px;height:591px}
.hero-photo{position:absolute;inset:0;background:linear-gradient(180deg,#6b6e6f 0%,#8a8c8a 40%,#a9a69c 75%,#7d7a72 100%)}
.hero-title{left:108px;top:186px;font-size:44px;font-weight:700;line-height:45px;color:#fff;text-transform:uppercase;width:560px}
.btn-green{background:var(--green);color:#fff;font-weight:500;text-transform:uppercase;display:flex;align-items:center;justify-content:center}
.hero-btn{left:108px;top:388px;width:152px;height:43px;font-size:14px}
.hero-arrow{top:260px;color:#fff;font-size:40px;opacity:.7}
.dots{left:565px;top:543px;display:flex;gap:8px}
.dots span{width:11px;height:11px;border:1.5px solid #fff;border-radius:50%}
.dots span.on{background:#fff}

.section-title{left:0;width:1200px;text-align:center;font-size:38px;font-weight:700;color:var(--grey-title);text-transform:uppercase}
.section-title em{font-style:normal;color:var(--green)}

/* cards */
.cards{display:flex;gap:12px}
.card{width:241px;border:1px solid var(--card-border);background:#fff;position:relative}
.card-photo{height:153px;background:linear-gradient(160deg,#8f9597,#c3c5c2 50%,#6e7275);position:relative;overflow:hidden}
.eye{position:absolute;right:8px;bottom:6px;width:24px;height:24px;border-radius:50%;background:#fff;display:flex;align-items:center;justify-content:center}
.card-body{padding:10px 8px 12px}
.meta{display:flex;gap:6px;margin-bottom:10px}
.tag{font-size:9px;height:20px;padding:0 8px;display:flex;align-items:center;border:1px solid #ccc;color:#555}
.tag.time{background:var(--green);border-color:var(--green);color:#fff}
.card-text{font-size:13px;line-height:19px;color:#222;font-weight:500}
.loc{font-size:10px;color:#333;margin:6px 0 12px;display:flex;align-items:center;gap:4px}
.card-actions{display:flex;gap:6px}
.btn-grey{background:var(--btn-grey);color:#fff;font-size:12px;font-weight:500;height:32px;display:flex;align-items:center;justify-content:center;text-transform:uppercase}
.heart{width:34px;height:32px;background:var(--green);display:flex;align-items:center;justify-content:center}
.arrow{position:absolute;font-size:44px;color:#333;font-weight:300}
.ribbon{position:absolute;left:-34px;top:26px;width:140px;transform:rotate(-45deg);background:#e53c2e;color:#fff;font-size:8px;text-align:center;padding:3px 0;text-transform:uppercase}
.btn-sm{font-size:9px;height:26px;padding:0 10px}
.btn-green.btn-sm{height:26px}

/* welcome */
.welcome{top:1256px;height:528px;background:var(--green-band)}
.welcome-photo{left:150px;top:78px;width:418px;height:356px;background:linear-gradient(135deg,#6e6f5a,#b7b49a 50%,#3f4038);clip-path:polygon(25% 0,75% 0,100% 50%,75% 100%,25% 100%,0 50%)}
.welcome-title{left:618px;top:94px;font-size:31px;font-weight:700;line-height:36px;color:#fff;text-transform:uppercase}
.welcome-copy{left:618px;top:174px;width:427px;font-size:12.3px;line-height:21.3px;color:#fff;text-align:justify}
.welcome-copy p+p{margin-top:12px}

/* companies */
.companies{top:2355px;height:320px;background:var(--green-band)}
.companies-title{left:0;top:70px;width:1200px;text-align:center;font-size:31px;font-weight:700;color:#fff;text-transform:uppercase}
.partner{top:150px;width:270px;height:97px;background:#fff;display:flex;align-items:center;justify-content:center;gap:10px;font-size:24px;font-weight:700;color:#3a6f37}
.partner i{width:24px;height:24px;background:#3a6f37;border-radius:50%}

/* services */
.services{top:2675px;height:738px}
.services-sub{left:0;top:160px;width:1200px;text-align:center;font-size:18px;font-weight:500}
.svc-label{font-size:17px;font-weight:500;color:#222}

/* resources */
.resources{top:3413px;height:516px;background:var(--light-bg)}
.res-card{left:179px;top:116px;width:841px;height:341px;background:#fff;box-shadow:0 0 12px rgba(0,0,0,.05)}
.res-photo{position:absolute;left:0;top:0;width:450px;height:341px;background:linear-gradient(150deg,#6a6a66,#a8a49b 50%,#5a5651)}
.res-title{left:481px;top:52px;width:340px;font-size:20px;font-weight:700;line-height:26px}
.res-copy{left:481px;top:120px;width:340px;font-size:13.5px;line-height:24px;color:#444}
.res-btn{left:481px;top:253px;width:135px;height:38px;font-size:13px}

/* newsletter */
.newsletter{top:3929px;height:167px;background:var(--green-band)}
.nl-title{left:151px;top:52px;font-size:23px;font-weight:700;color:#fff;text-transform:uppercase}
.nl-copy{left:151px;top:91px;width:360px;font-size:13px;line-height:19px;color:#fff}
.nl-form{left:586px;top:55px;width:463px;height:54px;background:#fff;display:flex;border:2px solid #fff}
.nl-form span{flex:1;display:flex;align-items:center;padding-left:20px;font-size:13px;color:#aaa}
.nl-form b{width:130px;background:var(--green);color:#fff;display:flex;align-items:center;justify-content:center;font-size:14px;font-weight:500}

/* footer */
.site-footer{top:4096px;height:375px;background:var(--footer);color:#fff}
.f-brand{left:100px;top:62px;display:flex;align-items:center;gap:14px}
.f-brand .brand-mark{width:68px;height:68px;background:#fff}
.f-brand .brand-name{color:#fff;font-size:22px;line-height:24px}
.socials{left:160px;top:160px;display:flex;gap:12px}
.socials span{width:40px;height:40px;border:2px solid #fff;border-radius:50%}
.f-col h4{font-size:17px;font-weight:700;text-transform:uppercase;margin-bottom:12px}
.f-col li{list-style:none;font-size:13px;line-height:25px}
.f-contact{font-size:13px;line-height:20px}
.f-input{width:238px;height:40px;background:#fff;color:#444;font-size:13px;padding:10px 12px;margin-bottom:8px}
.f-submit{width:100px;height:33px;font-size:13px;margin-left:138px}
.f-rule{left:100px;top:323px;width:1000px;height:1px;background:#555}
.copyright{left:0;top:340px;width:1200px;text-align:center;font-size:13px}
</style>
</head>
<body>
<div class="page">

<header class="site-header">
  <div class="abs brand"><span class="brand-mark"></span><span class="brand-name">Meridel<br>Bidding Group</span></div>
  <div class="abs phone">
    <span class="phone-icon"><svg width="16" height="16" viewBox="0 0 24 24"><path d="M6.6 10.8a15 15 0 0 0 6.6 6.6l2.2-2.2a1 1 0 0 1 1-.25 11 11 0 0 0 3.6.6 1 1 0 0 1 1 1V20a1 1 0 0 1-1 1A17 17 0 0 1 3 4a1 1 0 0 1 1-1h3.5a1 1 0 0 1 1 1 11 11 0 0 0 .6 3.6 1 1 0 0 1-.25 1z" fill="#8dc63f"/></svg></span>
    (555) 014-2870
  </div>
  <div class="abs finder-btn">Equipment Finder</div>
  <div class="abs lang">EN <svg width="10" height="6" viewBox="0 0 10 6"><path d="M1 1l4 4 4-4" stroke="#666" fill="none"/></svg></div>
  <nav>
    <svg class="home-icon" width="18" height="16" viewBox="0 0 16 14"><path d="M8 1l7 6h-2v6H3V7H1z" fill="#8dc63f"/></svg>
    <span class="nav-item home" style="left:474px">Home</span>
    <span class="nav-item" style="left:587px">About Us</span>
    <span class="nav-item" style="left:714px">Services</span>
    <span class="nav-item" style="left:823px">FAQ's</span>
    <span class="nav-item" style="left:936px">Auctions</span>
    <span class="nav-item" style="left:1063px">Contact</span>
  </nav>
</header>

<section class="hero">
  <div class="hero-photo" role="img" aria-label="Interior of a food manufacturing plant with a long stainless steel processing line"></div>
  <div class="abs arrow hero-arrow" style="left:58px">&#8249;</div>
  <div class="abs arrow hero-arrow" style="left:1118px">&#8250;</div>
  <h1 class="abs hero-title">Leaders in food manufacturing &amp; packaging equipment auctions</h1>
  <div class="abs btn-green hero-btn">Get Started</div>
  <div class="abs dots"><span class="on"></span><span></span><span></span><span></span></div>
</section>

<section class="upcoming" style="top:681px;height:575px">
  <h2 class="abs section-title" style="top:86px"><em>Upcoming</em> Auctions</h2>
  <div class="abs arrow" style="left:62px;top:290px">&#8249;</div>
  <div class="abs arrow" style="left:1116px;top:290px">&#8250;</div>
  <div class="abs cards" style="left:99px;top:165px">
    <article class="card">
      <div class="card-photo" role="img" aria-label="Industrial refrigeration condenser units"><span class="eye"><svg width="14" height="10" viewBox="0 0 14 10"><ellipse cx="7" cy="5" rx="6" ry="4" fill="none" stroke="#333"/><circle cx="7" cy="5" r="2" fill="#333"/></svg></span></div>
      <div class="card-body">
        <div class="meta"><span class="tag">20-Oct-2021</span><span class="tag time">10:00 AM</span></div>
        <p class="card-text">The standard Lorem Ipm passage, used since the 1500s</p>
        <p class="loc"><svg width="8" height="10" viewBox="0 0 8 10"><path d="M4 0a4 4 0 0 1 4 4c0 3-4 6-4 6S0 7 0 4a4 4 0 0 1 4-4z" fill="#333"/></svg>Multi Location California &amp; , CO</p>
        <div class="card-actions"><span class="btn-grey" style="width:138px">View Details</span><span class="heart"><svg width="16" height="14" viewBox="0 0 16 14"><path d="M8 13S1 8.5 1 4.5A3.5 3.5 0 0 1 8 3a3.5 3.5 0 0 1 7 1.5C15 8.5 8 13 8 13z" fill="#fff"/></svg></span></div>
      </div>
    </article>
    <article class="card">
      <div class="card-photo" role="img" aria-label="Stainless steel piping and heat exchanger"><span class="eye"><svg width="14" height="10" viewBox="0 0 14 10"><ellipse cx="7" cy="5" rx="6" ry="4" fill="none" stroke="#333"/><circle cx="7" cy="5" r="2" fill="#333"/></svg></span></div>
      <div class="card-body">
        <div class="meta"><span class="tag">20-Oct-2021</span><span class="tag time">10:00 AM</span></div>
        <p class="card-text">The standard Lorem Ipm passage, used since the 1500s</p>
        <p class="loc"><svg width="8" height="10" viewBox="0 0 8 10"><path d="M4 0a4 4 0 0 1 4 4c0 3-4 6-4 6S0 7 0 4a4 4 0 0 1 4-4z" fill="#333"/></svg>Multi Location California &amp; , CO</p>
        <div class="card-actions"><span class="btn-grey" style="width:138px">View Details</span><span class="heart"><svg width="16" height="14" viewBox="0 0 16 14"><path d="M8 13S1 8.5 1 4.5A3.5 3.5 0 0 1 8 3a3.5 3.5 0 0 1 7 1.5C15 8.5 8 13 8 13z" fill="#fff"/></svg></span></div>
      </div>
    </article>
    <article class="card">
      <div class="card-photo" role="img" aria-label="Food processing line with conveyors"><span class="eye"><svg width="14" height="10" viewBox="0 0 14 10"><ellipse cx="7" cy="5" rx="6" ry="4" fill="none" stroke="#333"/><circle cx="7" cy="5" r="2" fill="#333"/></svg></span></div>
      <div class="card-body">
        <div class="meta"><span class="tag">20-Oct-2021</span><span class="tag time">10:00 AM</span></div>
        <p class="card-text">The standard Lorem Ipm passage, used since the 1500s</p>
        <p class="loc"><svg width="8" height="10" viewBox="0 0 8 10"><path d="M4 0a4 4 0 0 1 4 4c0 3-4 6-4 6S0 7 0 4a4 4 0 0 1 4-4z" fill="#333"/></svg>Multi Location California &amp; , CO</p>
        <div class="card-actions"><span class="btn-grey" style="width:138px">View Details</span><span class="heart"><svg width="16" height="14" viewBox="0 0 16 14"><path d="M8 13S1 8.5 1 4.5A3.5 3.5 0 0 1 8 3a3.5 3.5 0 0 1 7 1.5C15 8.5 8 13 8 13z" fill="#fff"/></svg></span></div>
      </div>
    </article>
    <article class="card">
      <div class="card-photo" role="img" aria-label="Processing plant valves and tanks"><span class="eye"><svg width="14" height="10" viewBox="0 0 14 10"><ellipse cx="7" cy="5" rx="6" ry="4" fill="none" stroke="#333"/><circle cx="7" cy="5" r="2" fill="#333"/></svg></span></div>
      <div class="card-body">
        <div class="meta"><span class="tag">20-Oct-2021</span><span class="tag time">10:00 AM</span></div>
        <p class="card-text">The standard Lorem Ipm passage, used since the 1500s</p>
        <p class="loc"><svg width="8" height="10" viewBox="0 0 8 10"><path d="M4 0a4 4 0 0 1 4 4c0 3-4 6-4 6S0 7 0 4a4 4 0 0 1 4-4z" fill="#333"/></svg>Multi Location California &amp; , CO</p>
        <div class="card-actions"><span class="btn-grey" style="width:138px">View Details</span><span class="heart"><svg width="16" height="14" viewBox="0 0 16 14"><path d="M8 13S1 8.5 1 4.5A3.5 3.5 0 0 1 8 3a3.5 3.5 0 0 1 7 1.5C15 8.5 8 13 8 13z" fill="#fff"/></svg></span></div>
      </div>
    </article>
  </div>
</section>

<section class="welcome">
  <div class="abs welcome-photo" role="img" aria-label="Auctioneers at a podium during a live sale"></div>
  <h2 class="abs welcome-title">Welcome to<br>Meridel Bidding Group</h2>
  <div class="abs welcome-copy">
    <p>Meridel Bidding Group is a full-service asset-management company specializing in food manufacturing and packaging equipment. Our goal at Meridel Bidding Group is to provide our customers with a range of options to liquidate their assets. A few of the services we offer are appraisals, asset management, live onsite auctions, online auctions and orderly negotiated sales. We help our customers determine the best options to maximize returns within their given parameters.</p>
    <p>Our experienced staff is committed to providing our customers with satisfaction through hard work, integrity, communication and transparency. It is those characteristics of the people behind Meridel Bidding Group that help make this company a top choice in managing surplus assets for companies of all sizes.</p>
  </div>
</section>

<section class="past" style="top:1784px;height:571px">
  <h2 class="abs section-title" style="top:86px"><em>Past</em> Auctions</h2>
  <div class="abs arrow" style="left:78px;top:290px">&#8249;</div>
  <div class="abs arrow" style="left:1130px;top:290px">&#8250;</div>
  <div class="abs cards" style="left:115px;top:163px">
    <article class="card" style="overflow:hidden">
      <div class="card-photo" role="img" aria-label="Packaging line with blue conveyors"><span class="eye"><svg width="14" height="10" viewBox="0 0 14 10"><ellipse cx="7" cy="5" rx="6" ry="4" fill="none" stroke="#333"/><circle cx="7" cy="5" r="2" fill="#333"/></svg></span></div>
      <span class="ribbon">Completed Auction</span>
      <div class="card-body">
        <div class="meta"><span class="tag">20-Oct-2021</span><span class="tag time">10:00 AM</span></div>
        <p class="card-text">Surplus Assets to National Premium Dessert Supplier and</p>
        <p class="loc"><svg width="8" height="10" viewBox="0 0 8 10"><path d="M4 0a4 4 0 0 1 4 4c0 3-4 6-4 6S0 7 0 4a4 4 0 0 1 4-4z" fill="#333"/></svg>Multi Location California &amp; , CO</p>
        <div class="card-actions"><span class="btn-grey btn-sm">View Details</span><span class="btn-green btn-sm">Go to Online Auction</span></div>
      </div>
    </article>
    <article class="card" style="overflow:hidden">
      <div class="card-photo" role="img" aria-label="Long production hall with conveyor"><span class="eye"><svg width="14" height="10" viewBox="0 0 14 10"><ellipse cx="7" cy="5" rx="6" ry="4" fill="none" stroke="#333"/><circle cx="7" cy="5" r="2" fill="#333"/></svg></span></div>
      <span class="ribbon">Completed Auction</span>
      <div class="card-body">
        <div class="meta"><span class="tag">20-Oct-2021</span><span class="tag time">10:00 AM</span></div>
        <p class="card-text">Surplus Assets to National Premium Dessert Supplier and</p>
        <p class="loc"><svg width="8" height="10" viewBox="0 0 8 10"><path d="M4 0a4 4 0 0 1 4 4c0 3-4 6-4 6S0 7 0 4a4 4 0 0 1 4-4z" fill="#333"/></svg>Multi Location California &amp; , CO</p>
        <div class="card-actions"><span class="btn-grey btn-sm">View Details</span><span class="btn-green btn-sm">Go to Online Auction</span></div>
      </div>
    </article>
    <article class="card" style="overflow:hidden">
      <div class="card-photo" role="img" aria-label="Stainless steel production equipment"><span class="eye"><svg width="14" height="10" viewBox="0 0 14 10"><ellipse cx="7" cy="5" rx="6" ry="4" fill="none" stroke="#333"/><circle cx="7" cy="5" r="2" fill="#333"/></svg></span></div>
      <span class="ribbon">Completed Auction</span>
      <div class="card-body">
        <div class="meta"><span class="tag">20-Oct-2021</span><span class="tag time">10:00 AM</span></div>
        <p class="card-text">Surplus Assets to National Premium Dessert Supplier and</p>
        <p class="loc"><svg width="8" height="10" viewBox="0 0 8 10"><path d="M4 0a4 4 0 0 1 4 4c0 3-4 6-4 6S0 7 0 4a4 4 0 0 1 4-4z" fill="#333"/></svg>Multi Location California &amp; , CO</p>
        <div class="card-actions"><span class="btn-grey btn-sm">View Details</span><span class="btn-green btn-sm">Go to Online Auction</span></div>
      </div>
    </article>
    <article class="card" style="overflow:hidden">
      <div class="card-photo" role="img" aria-label="Industrial mixing machinery"><span class="eye"><svg width="14" height="10" viewBox="0 0 14 10"><ellipse cx="7" cy="5" rx="6" ry="4" fill="none" stroke="#333"/><circle cx="7" cy="5" r="2" fill="#333"/></svg></span></div>
      <span class="ribbon">Completed Auction</span>
      <div class="card-body">
        <div class="meta"><span class="tag">20-Oct-2021</span><span class="tag time">10:00 AM</span></div>
        <p class="card-text">Surplus Assets to National Premium Dessert Supplier and</p>
        <p class="loc"><svg width="8" height="10" viewBox="0 0 8 10"><path d="M4 0a4 4 0 0 1 4 4c0 3-4 6-4 6S0 7 0 4a4 4 0 0 1 4-4z" fill="#333"/></svg>Multi Location California &amp; , CO</p>
        <div class="card-actions"><span class="btn-grey btn-sm">View Details</span><span class="btn-green btn-sm">Go to Online Auction</span></div>
      </div>
    </article>
  </div>
</section>

<section class="companies">
  <h2 class="abs companies-title">Companies We've Worked With</h2>
  <div class="abs partner" style="left:168px"><i></i>Oakline Foods</div>
  <div class="abs partner" style="left:465px"><i></i>Harbor Creek Foods</div>
  <div class="abs partner" style="left:762px"><i></i>Oakline Foods</div>
</section>

<section class="services">
  <h2 class="abs section-title" style="top:90px"><em>Our</em> Services</h2>
  <p class="abs services-sub">Below are a list of our services please contact us for more information.</p>
  <svg class="abs" style="left:0;top:0" width="1200" height="738" viewBox="0 0 1200 738">
    <g fill="none" stroke="#9a9a9a" stroke-width="1.5">
      <circle cx="599" cy="429" r="151" stroke="#8dc63f" stroke-width="2"/>
      <path d="M425 273h50l35 42"/>
      <path d="M835 260h-50l-45 40"/>
      <path d="M349 434h95"/>
      <path d="M844 425h-96"/>
      <path d="M448 599h45l40-44"/>
      <path d="M835 603h-70l-105-45"/>
    </g>
    <g fill="#fff" stroke="#9a9a9a" stroke-width="1.5">
      <circle cx="510" cy="315" r="6"/><circle cx="740" cy="300" r="6"/>
      <circle cx="448" cy="434" r="6"/><circle cx="748" cy="425" r="6"/>
      <circle cx="533" cy="555" r="6"/><circle cx="660" cy="558" r="6"/>
    </g>
    <g fill="#fff" stroke="#8dc63f" stroke-width="2">
      <circle cx="380" cy="273" r="45"/><circle cx="304" cy="434" r="45"/><circle cx="403" cy="599" r="45"/>
    </g>
    <g fill="#fff" stroke="#888" stroke-width="2">
      <circle cx="790" cy="260" r="45"/><circle cx="889" cy="425" r="45"/><circle cx="790" cy="603" r="45"/>
    </g>
    <g fill="none" stroke="#8dc63f" stroke-width="1.8">
      <rect x="362" y="262" width="34" height="26"/><path d="M368 262v-10h10v10M384 262v-14h8v14"/>
      <rect x="290" y="414" width="26" height="36"/><path d="M296 424h14M296 432h14M296 440h8"/><path d="M306 444l6 6 10-12"/>
      <circle cx="403" cy="590" r="12"/><path d="M403 583v14M389 620v-12M417 620v-12M403 620v-8"/>
    </g>
    <g fill="none" stroke="#777" stroke-width="1.8">
      <path d="M768 262l10-10 12 6 12-6 10 10-14 12-8-6-8 6z"/>
      <rect x="876" y="410" width="26" height="34"/><path d="M882 418h4M892 418h4M882 428h4M892 428h4M887 444v-8"/>
      <circle cx="790" cy="603" r="16"/><path d="M786 596h8M786 603h8M790 592v22"/>
    </g>
    <text x="599" y="420" text-anchor="middle" font-family="Roboto,Arial,sans-serif" font-size="24" font-weight="700" fill="#55585b">Meridel</text>
    <text x="599" y="450" text-anchor="middle" font-family="Roboto,Arial,sans-serif" font-size="24" font-weight="700" fill="#55585b">Bidding Group</text>
  </svg>
  <span class="abs svc-label" style="left:162px;top:262px">Asset Management</span>
  <span class="abs svc-label" style="left:845px;top:250px">Orderly Negotiated Sales</span>
  <span class="abs svc-label" style="left:162px;top:424px">Appraisals</span>
  <span class="abs svc-label" style="left:947px;top:415px">Real Estate</span>
  <span class="abs svc-label" style="left:278px;top:600px">Auctions</span>
  <span class="abs svc-label" style="left:849px;top:593px">Turnkey Operations</span>
</section>

<section class="resources">
  <h2 class="abs section-title" style="top:46px"><em>Latest</em> Resources</h2>
  <div class="abs arrow" style="left:136px;top:250px">&#8249;</div>
  <div class="abs arrow" style="left:1044px;top:250px">&#8250;</div>
  <div class="abs res-card">
    <div class="res-photo" role="img" aria-label="Used industrial food machine on a wooden pallet"></div>
    <h3 class="abs res-title">The standard Lorem Ipsum passage, used since the 1500s</h3>
    <p class="abs res-copy">Lorem ipsum dolor sit amet, consectetur adipiscing elit, sed do eiusmod tempor incididunt ut labore et dolore magna aliqua. Ut enim ad minim veniam, quis nostrud exercitation ullamco laboris nisi ut aliquip ex ea commodo consequat.</p>
    <div class="abs btn-green res-btn">Learn More</div>
  </div>
</section>

<section class="newsletter">
  <h2 class="abs nl-title">Subscribe to our newsletters</h2>
  <p class="abs nl-copy">If you would like to join our mailing list, please use the sign up now button below.</p>
  <div class="abs nl-form"><span>Enter email address</span><b>SUBSCRIBE</b></div>
</section>

<footer class="site-footer">
  <div class="abs f-brand"><span class="brand-mark"></span><span class="brand-name">Meridel<br>Bidding Group</span></div>
  <div class="abs socials" role="img" aria-label="Social media links"><span></span><span></span><span></span></div>
  <div class="abs f-col" style="left:436px;top:62px">
    <h4>Site Map</h4>
    <ul><li>Home</li><li>Services</li><li>FAQ's</li><li>Auctions</li><li>Equipment Finder</li><li>Mailing List</li><li>Resources</li><li>Contact Us</li></ul>
  </div>
  <div class="abs f-col" style="left:606px;top:62px">
    <h4>Find Us</h4>
    <p class="f-contact"><svg width="10" height="13" viewBox="0 0 8 10"><path d="M4 0a4 4 0 0 1 4 4c0 3-4 6-4 6S0 7 0 4a4 4 0 0 1 4-4z" fill="#fff"/></svg> Meridel Office</p>
    <p class="f-contact" style="margin:6px 0 0 24px">48 Fairfield Lane Linden,<br>ND 50010</p>
    <p class="f-contact" style="margin-top:8px">&#9990; (555) 014-2870</p>
  </div>
  <div class="abs f-col" style="left:863px;top:62px">
    <h4>Send a Message</h4>
    <div class="f-input">Name</div>
    <div class="f-input">Email</div>
    <div class="f-input" style="height:58px">Message</div>
    <div class="btn-green f-submit">SUBMIT</div>
  </div>
  <div class="abs f-rule"></div>
  <p class="abs copyright">Copyright © 2021 Meridel Bidding Group . All rights reserved.</p>
</footer>

</div>
</body>
</html>
```